Hi! We require a design for business cards for directors and head teachers of an international daycare for children 0 - 9. We are family-owned, -operated and -oriented. We have six locations, looking to franchise. Our USPs are: 1) Flexibility 2) Quality teachers 3) International culture 4) Best nutrition We are quality teachers and professional caretakers, but with creativity and personality! Business cards should be playful (but no Comic Sans or baby hand prints), colorful (but no rainbows), and have some breathing space. It should be obvious from the business card that we're a daycare. In 2020 we'll be launching our new website based on this design: https://plomvane.io/47K2RQLWZTD The font in the new website will be Houschka (medium, demibold, bold). We will keep our current logo, included in the files here. There are also screenshots of some designs we like. Show us your best! :)

Industry/Entity Type

Childcare

Contact Information for Business Card

Lotte de Vries-Bakhuis
Communications Wizard
Poppel Hoek International Daycare
Kastanjeweg 47 B, 2316 KR Leiden
www.poppelhoek.nl
+31 647315082

Font styles to use
Serif
Sans Serif

Colors

Designer to choose colors to be used in the design.

Requirements
Must have
• Color

```html
<!DOCTYPE html>
<html lang="en">
<head>
<meta charset="utf-8">
<title>Poppel Hoek – Business Card</title>
<link rel="stylesheet" href="https://fonts.googleapis.com/css2?family=Raleway:wght@300;400&family=Open+Sans:wght@400&display=swap">
<style>
  :root {
    --plum: #bd3a8f;
    --pink: #ef4b7c;
    --sun: #f9d94f;
    --ink: #3a3a3a;
    --backdrop: #eae9e9;
  }
  * { margin: 0; padding: 0; box-sizing: border-box; }
  html, body { width: 1200px; height: 1010px; overflow: hidden; }
  body {
    background: var(--backdrop);
    position: relative;
    font-family: "Open Sans", Arial, sans-serif;
    color: var(--ink);
  }
  .card {
    position: absolute;
    top: 157px;
    width: 400px;
    height: 696px;
    background: var(--sun);
    overflow: hidden;
  }
  .card--front { left: 186px; }
  .card--back { left: 614px; }

  .card__pattern {
    position: absolute;
    left: 0;
    top: 0;
    width: 400px;
    display: block;
  }

  .brand-name {
    position: absolute;
    left: 0;
    top: 322px;
    width: 100%;
    text-align: center;
    font-family: "Raleway", Arial, sans-serif;
    font-weight: 300;
    font-size: 30px;
    letter-spacing: 6px;
    color: var(--sun);
  }

  .contact {
    position: absolute;
    left: 0;
    top: 336px;
    width: 100%;
    text-align: center;
  }
  .contact__name,
  .contact__role {
    font-family: "Raleway", Arial, sans-serif;
    font-weight: 400;
    font-size: 27px;
    line-height: 42px;
  }
  .contact__org {
    margin-top: 60px;
    font-size: 18px;
    line-height: 30px;
  }
  .contact__web {
    margin-top: 30px;
    font-size: 18px;
  }
  .contact__phone {
    margin-top: 30px;
    font-size: 18px;
  }
</style>
</head>
<body>
  <section class="card card--front">
    <svg class="card__pattern" width="400" height="540" viewBox="0 0 400 540" role="img" aria-label="Playful paint drips flowing from plum into pink into yellow">
      <defs>
        <linearGradient id="front-drip" x1="0" y1="0" x2="0" y2="1">
          <stop offset="0" stop-color="#bd3a8f"/>
          <stop offset="0.34" stop-color="#bd3a8f"/>
          <stop offset="0.52" stop-color="#ef4b7c"/>
          <stop offset="0.72" stop-color="#ef4b7c"/>
          <stop offset="1" stop-color="#f9d94f"/>
        </linearGradient>
      </defs>
      <rect width="400" height="540" fill="url(#front-drip)"/>
    </svg>
    <p class="brand-name">POPPEL HOEK</p>
  </section>

  <section class="card card--back">
    <svg class="card__pattern" width="400" height="300" viewBox="0 0 400 300" role="img" aria-label="Playful paint drips flowing from plum into pink into yellow">
      <defs>
        <linearGradient id="back-drip" x1="0" y1="0" x2="0" y2="1">
          <stop offset="0" stop-color="#bd3a8f"/>
          <stop offset="0.22" stop-color="#bd3a8f"/>
          <stop offset="0.5" stop-color="#ef4b7c"/>
          <stop offset="0.62" stop-color="#ef4b7c"/>
          <stop offset="1" stop-color="#f9d94f"/>
        </linearGradient>
      </defs>
      <rect width="400" height="300" fill="url(#back-drip)"/>
    </svg>
    <div class="contact">
      <p class="contact__name">Lotte de Vries-Bakhuis</p>
      <p class="contact__role">Communications Wizard</p>
      <p class="contact__org">Poppel Hoek International Daycare<br>Kastanjeweg 47 B, 2316 KR Leiden</p>
      <p class="contact__web">www.poppelhoek.nl</p>
      <p class="contact__phone">+31 647 315 082</p>
    </div>
  </section>
</body>
</html>
```